Brightfold Partners Website

Brightfold Partners Advisory Services is a company which provides specialised advise in carbon markets, climate policy, landscapes, resilience and change. We are based in Australia but the majority of our business is global. Our clients range from governments to large corporates and not for profit organisations.
Our focus is on developing the capabilities of government officials, business decision makers and land managers so they can better navigate the complexity of climate change and sustainability.
We are looking for a website that is consistent with the high end professional services which we provide to serious players.
I have attached two versions of our logo. I have also attached the back of our business card so you can get a sense of what we hand to potential clients.

Target Market(s)

Professional individuals, decision makers, board members etc, government officials.

Industry/Entity Type

Government

Number of Pages Required

4 page

Font styles to use
Serif
Sans Serif

Requirements
Must have
• Please provide
• 1. Home page
• 2. Service page template
• 3. Contact page
• 4. Lead expert profile page

```html
<!DOCTYPE html>
<html lang="en">
<head>
<meta charset="utf-8">
<title>Brightfold Partners Advisory Services</title>
<link rel="stylesheet" href="https://fonts.googleapis.com/css2?family=Open+Sans:wght@300;400;600;700&display=swap">
<style>
  :root {
    --page-bg: #e9e9e7;
    --panel: #ffffff;
    --contact-bg: #efefec;
    --footer-bg: #121212;
    --brand-blue: #1f7fc4;
    --link-blue: #2a78b6;
    --heading: #2f2f2f;
    --body-text: #8a8a8a;
    --muted: #a5a5a5;
    --rule: #e2e2e2;
    --field-border: #cfcfcf;
    --white: #ffffff;
  }
  * { box-sizing: border-box; margin: 0; padding: 0; }
  html, body { width: 676px; height: 1200px; overflow: hidden; }
  body {
    background: var(--page-bg);
    font-family: "Open Sans", Arial, sans-serif;
    color: var(--body-text);
    position: relative;
  }
  .site { position: absolute; left: 21px; top: 13px; width: 634px; height: 1171px; background: var(--panel); border-top: 3px solid var(--brand-blue); }

  /* header */
  .site-header { position: absolute; left: 0; top: 0; width: 634px; height: 75px; background: linear-gradient(#ffffff, #f6f6f6); }
  .brand { position: absolute; left: 17px; top: 22px; display: flex; align-items: center; gap: 7px; }
  .brand-dot { width: 20px; height: 20px; border-radius: 50%; background: #8c8c8c; }
  .brand-name { font-size: 13px; line-height: 15px; letter-spacing: 2px; color: #3a3a3a; font-weight: 400; }
  .top-contact { position: absolute; top: 22px; font-size: 7px; color: #8a8a8a; }
  .top-contact.email { left: 295px; }
  .top-contact.phone { left: 440px; }
  .search { position: absolute; left: 527px; top: 16px; width: 90px; height: 17px; border: 1px solid #d6d6d6; border-radius: 9px; background: #fff; font-size: 7px; color: #aaa; padding: 3px 8px; }
  .main-nav { position: absolute; left: 372px; top: 41px; display: flex; gap: 0; }
  .main-nav a { font-size: 6.5px; font-weight: 700; color: var(--brand-blue); text-decoration: none; padding: 7px 7px; height: 21px; }
  .main-nav a.active { background: var(--brand-blue); color: #fff; border-radius: 2px; }
  .social { position: absolute; left: 561px; top: 45px; display: flex; gap: 3px; }
  .social span { width: 15px; height: 15px; border-radius: 50%; border: 1px solid #d0d0d0; background: #fff; }

  /* hero */
  .hero { position: absolute; left: 0; top: 75px; width: 634px; height: 263px;
    background: linear-gradient(180deg, #e6e6e6 0%, #cfd1d2 45%, #9a9c9e 70%, #8a8b8c 100%); }

  /* intro */
  .intro-title { position: absolute; left: 20px; top: 368px; width: 594px; text-align: center; font-size: 19.5px; line-height: 27px; font-weight: 300; color: var(--heading); }
  .intro-text { position: absolute; left: 17px; top: 433px; width: 600px; height: 37px; overflow: hidden; text-align: center; font-size: 8px; line-height: 12.3px; color: var(--muted); }
  .intro-rule { position: absolute; left: 17px; top: 472px; width: 600px; border-top: 1px solid var(--rule); }
  .intro-note { position: absolute; left: 0; top: 499px; width: 634px; text-align: center; font-size: 7px; color: var(--muted); }
  .section-rule { position: absolute; left: 47px; top: 531px; width: 540px; border-top: 1px solid var(--rule); }

  /* services */
  .service { position: absolute; width: 180px; text-align: center; }
  .service h3 { font-size: 10.5px; line-height: 14px; font-weight: 400; color: var(--link-blue); }
  .service p { font-size: 7.5px; line-height: 12.5px; color: #8a8a8a; }
  .c1 { left: 34px; } .c2 { left: 240px; } .c3 { left: 446px; }
  .r1 { top: 557px; } .r2 { top: 634px; }

  /* contact */
  .contact { position: absolute; left: 0; top: 716px; width: 634px; height: 326px; background: var(--contact-bg); }
  .contact-title { position: absolute; left: 16px; top: 27px; font-size: 19px; font-weight: 300; color: #111; }
  .contact-title b { font-weight: 700; }
  .field-label { position: absolute; font-size: 7px; color: #777; }
  .field { position: absolute; background: #fff; border: 1px solid var(--field-border); border-radius: 2px; }
  .send { position: absolute; left: 16px; top: 275px; width: 81px; height: 23px; background: var(--brand-blue); border-radius: 3px; color: #fff; font-size: 8.5px; text-align: center; line-height: 23px; }
  .info { position: absolute; left: 325px; width: 292px; }
  .info h4 { font-size: 10.5px; font-weight: 400; color: var(--link-blue); margin-bottom: 9px; }
  .info h4 b { font-weight: 700; }
  .info p { font-size: 7px; line-height: 12.5px; color: #777; }
  .info p b { color: #555; font-weight: 700; }
  .info a { color: var(--link-blue); text-decoration: none; }
  .info-rule { position: absolute; left: 325px; width: 292px; border-top: 1px solid #dcdcd8; }

  /* footer */
  .site-footer { position: absolute; left: 0; top: 1040px; width: 634px; height: 128px; background: var(--footer-bg); }
  .footer-title { position: absolute; left: 16px; top: 27px; font-size: 12px; font-weight: 300; color: #fff; }
  .footer-text { position: absolute; left: 16px; top: 50px; width: 390px; font-size: 6.3px; line-height: 13px; color: #6e6e6e; }
  .footer-text a { color: #fff; text-decoration: none; }
  .footer-rule { position: absolute; left: 16px; top: 99px; width: 384px; border-top: 1px solid #2a2a2a; }
  .footer-contact { position: absolute; left: 479px; top: 28px; color: #fff; }
  .footer-contact .label { font-size: 5.8px; font-weight: 700; }
  .footer-contact .phone { font-size: 13.5px; font-weight: 700; line-height: 17px; }
  .footer-contact .mail { font-size: 6.5px; margin-top: 4px; }
  .footer-social { position: absolute; left: 483px; top: 74px; display: flex; gap: 3px; }
  .footer-social span { width: 15px; height: 15px; border-radius: 50%; background: #fff; }
</style>
</head>
<body>
<div class="site">
  <header class="site-header">
    <div class="brand"><span class="brand-dot"></span><span class="brand-name">BRIGHTFOLD<br>PARTNERS</span></div>
    <span class="top-contact email">Email: dana.whitlock@brightfold.com.au</span>
    <span class="top-contact phone">Phone: +61 412 555 830</span>
    <div class="search">Search..</div>
    <nav class="main-nav">
      <a class="active" href="#">HOME</a><a href="#">SERVICES</a><a href="#">LEAD EXPERT</a><a href="#">CONTACT</a>
    </nav>
    <div class="social"><span></span><span></span><span></span></div>
  </header>

  <div class="hero" role="img" aria-label="Photo of business people in suits lifting a rising blue arrow chart in front of a grey city skyline"></div>

  <h1 class="intro-title">Brightfold Partners provides expert advisory services in carbon markets, climate policy, landscapes and change.</h1>
  <p class="intro-text">Our focus is on developing the capabilities of government officials, business decision makers and land managers so they can better navigate the complexity of climate change &amp; sustainability. Dana Whitlock leads all of Brightfold Partners’ advisory engagements. Her profile is available here. We provide advisory services across a number of specialised areas. However, all of our advisory services are tailored to the situation and needs of the client, so no two engagements are the same.</p>
  <div class="intro-rule"></div>
  <p class="intro-note">A selection of recent engagements is provided below.</p>
  <div class="section-rule"></div>

  <div class="service c1 r1"><h3>Corporate Advisory on Carbon Markets</h3><p>Lorem ipsum dolor sit amet, consectetur adipiscing elit. Curabitur imperdiet hendrerit volutpat.</p></div>
  <div class="service c2 r1"><h3>Project Mechanisms (carbon credits &amp; offsets)</h3><p>Lorem ipsum dolor sit amet, consectetur adipiscing elit. Curabitur imperdiet hendrerit volutpat.</p></div>
  <div class="service c3 r1"><h3>Monitoring, Reporting &amp; Verification</h3><p>Lorem ipsum dolor sit amet, consectetur adipiscing elit. Curabitur imperdiet hendrerit volutpat.</p></div>
  <div class="service c1 r2"><h3>Institutional Arrangements</h3><p>Lorem ipsum dolor sit amet, consectetur adipiscing elit. Curabitur imperdiet hendrerit volutpat.</p></div>
  <div class="service c2 r2"><h3>Training &amp; Coaching</h3><p>Lorem ipsum dolor sit amet, consectetur adipiscing elit. Curabitur imperdiet hendrerit volutpat.</p></div>
  <div class="service c3 r2"><h3>China’s Carbon Markets</h3><p>Lorem ipsum dolor sit amet, consectetur adipiscing elit. Curabitur imperdiet hendrerit volutpat.</p></div>

  <section class="contact">
    <h2 class="contact-title"><b>Contact</b> Us</h2>
    <span class="field-label" style="left:16px;top:58px">Your name *</span>
    <div class="field" style="left:16px;top:70px;width:139px;height:19px"></div>
    <span class="field-label" style="left:170px;top:58px">Your email address *</span>
    <div class="field" style="left:170px;top:70px;width:139px;height:19px"></div>
    <span class="field-label" style="left:16px;top:98px">Subject</span>
    <div class="field" style="left:16px;top:110px;width:293px;height:19px"></div>
    <span class="field-label" style="left:16px;top:138px">Message *</span>
    <div class="field" style="left:16px;top:151px;width:293px;height:113px"></div>
    <div class="send">Send Message</div>

    <div class="info" style="top:47px"><h4>Get in <b>touch</b></h4><p>Please contact us if you would like to explore how Brightfold Partners can support your efforts in climate change &amp; sustainability.</p></div>
    <div class="info-rule" style="top:104px"></div>
    <div class="info" style="top:118px"><h4>The <b>Office</b></h4><p><b>Address:</b> 1234 Street Name, City Name, United States<br><b>Phone:</b>+61 412 555 830<br><b>Email:</b> <a href="#">dana.whitlock@brightfold.com.au</a></p></div>
    <div class="info-rule" style="top:187px"></div>
    <div class="info" style="top:201px"><h4>Business <b>Hours</b></h4><p>Monday – Friday 9am to 5pm<br>Saturday – 9am to 2pm<br>Sunday – Closed</p></div>
  </section>

  <footer class="site-footer">
    <h2 class="footer-title">Brightfold Partners Advisory Services</h2>
    <p class="footer-text">Brightfold Partners provides expert advisory services in carbon markets, climate policy, landscapes and change. Our focus is on developing the capabilities of government officials, business decision makers and land managers so they can better navigate the complexity of climate change &amp; sustainability... <a href="#">View More</a></p>
    <div class="footer-rule"></div>
    <div class="footer-contact">
      <div class="label">CONTACT US</div>
      <div class="phone">+61 412 555 830</div>
      <div class="mail">Email: dana.whitlock@brightfold.com.au</div>
    </div>
    <div class="footer-social"><span></span><span></span><span></span></div>
  </footer>
</div>
</body>
</html>
```